Business Card design

I would like to redo the business cards we have. I want a group card and then individual cards made for each doctor. I like the format of the card attached.

```html
<!DOCTYPE html>
<html lang="en">
<head>
<meta charset="utf-8">
<title>Harborview Oncology – Business Cards</title>
<link href="https://fonts.googleapis.com/css2?family=Montserrat:wght@700;800&family=Arimo:wght@400&display=swap" rel="stylesheet">
<style>
  :root{
    --bg:#e6e6e4;
    --navy:#065a8b;
    --sky:#3598d3;
    --white:#ffffff;
    --grey:#6f6f6f;
  }
  *{margin:0;padding:0;box-sizing:border-box}
  html,body{width:1200px;height:801px;overflow:hidden;background:var(--bg)}
  .stage{position:relative;width:1200px;height:801px}
  .card{position:absolute;top:243px;width:550px;height:314px;overflow:hidden;box-shadow:0 6px 18px rgba(0,0,0,.18)}
  .card--front{left:35px;background:var(--white)}
  .card--back{left:615px;background:var(--navy)}
  .wave{position:absolute;inset:0}
  .corner-mark{position:absolute;top:12px;right:12px;width:14px;height:14px;background:var(--navy)}
  .doctor-name{position:absolute;top:34px;right:70px;font:800 22px/1 "Montserrat",sans-serif;color:var(--sky)}
  .brand{font-family:"Montserrat",sans-serif;font-weight:800;color:var(--navy);line-height:1.05;display:flex;align-items:center;gap:10px}
  .brand__square{width:16px;height:16px;background:var(--sky);flex:none}
  .card--front .brand{position:absolute;left:52px;top:112px;font-size:26px}
  .address{position:absolute;left:100px;top:218px;font:400 14px/1.35 "Arimo",sans-serif;color:var(--grey)}
  .phones{position:absolute;right:28px;top:178px;font:400 14px/1.5 "Arimo",sans-serif;color:var(--white)}
  .phones li,.locations li.tel{list-style:none;display:flex;align-items:center;gap:6px}
  .phones li{justify-content:flex-end}
  .icon{width:12px;height:12px;flex:none}
  .locations{position:absolute;left:30px;top:24px;font:400 12.5px/1.32 "Arimo",sans-serif;color:var(--white)}
  .location{margin-bottom:10px}
  .location li.tel{padding-left:4px}
  .card--back .brand{position:absolute;right:30px;bottom:58px;color:var(--white);font-size:29px}
</style>
</head>
<body>
<main class="stage">

  <section class="card card--front" aria-label="Business card front">
    <svg class="wave" viewBox="0 0 550 314" preserveAspectRatio="none" aria-hidden="true">
      <path d="M550,40 C444,50 390,102 358,174 C322,256 212,292 20,314 L44,314 C228,298 330,264 365,182 C395,112 447,62 550,51 Z" fill="var(--sky)"/>
      <path d="M550,60 C452,70 404,118 374,188 C340,268 236,302 62,314 L550,314 Z" fill="var(--navy)"/>
    </svg>
    <div class="corner-mark"></div>
    <h1 class="doctor-name">Leena Marsh, M.D</h1>
    <div class="brand"><span class="brand__square"></span><span>Harborview<br>Oncology, PA</span></div>
    <p class="address">412 North Elm Street<br>Linden, New Jersey 07036</p>
    <ul class="phones">
      <li>(555) 214-3370
        <svg class="icon" viewBox="0 0 24 24"><path d="M6.6 10.8a15 15 0 006.6 6.6l2.2-2.2a1 1 0 011-.25 11.4 11.4 0 003.6.57 1 1 0 011 1V20a1 1 0 01-1 1A17 17 0 013 4a1 1 0 011-1h3.5a1 1 0 011 1c0 1.25.2 2.45.57 3.57a1 1 0 01-.25 1z" fill="var(--white)"/></svg></li>
      <li>(555) 214-3391
        <svg class="icon" viewBox="0 0 24 24"><path d="M6 3h9l3 3v4H6z M3 10h18v10H3z" fill="none" stroke="var(--white)" stroke-width="2"/></svg></li>
    </ul>
  </section>

  <section class="card card--back" aria-label="Business card back">
    <div class="locations">
      <div class="location">
        <p>Parkside Medical Office<br>90 Mill Street | Suite 200<br>Riverton, New Jersey 07109</p>
        <ul><li class="tel">(555) 751-8880</li><li class="tel">(555) 751-8950</li></ul>
      </div>
      <div class="location">
        <p>Westbrook Ambulatory Care Pavilion<br>18 Lake Road | Suite 2<br>Glenfield, New Jersey 07050</p>
        <ul><li class="tel">(555) 630-1200</li><li class="tel">(555) 630-1245</li></ul>
      </div>
      <div class="location">
        <p>412 North Elm Street<br>Linden, New Jersey 07036</p>
        <ul><li class="tel">(555) 214-3370</li><li class="tel">(555) 214-3391</li></ul>
      </div>
    </div>
    <div class="brand"><span class="brand__square"></span><span>Harborview<br>Oncology, PA</span></div>
  </section>

</main>
</body>
</html>
```